Artist needs a Wordpress Website design to market my original paintings

Mira Castellan Gallery.com
Artist - Original Abstract Paintings

Artist needs classy and elegant WORDPRESS website to market my Original Paintings.
What sets these paintings apart?
Each one was inspired by the inner connection between the artist and the individual destined to receive the painting. Paintings are priced high end and require a website to reflect their high quality.
Website must be responsive on all devices. eg. mobile, laptop and desktop. It must have a shopping cart in order to complete sales.
The domain name miracastellangallery.com has already been purchased and is hosted on Corvanet.
I want it to be very easy to navigate and also easy for me to add and edit more images and content.
I have no official logo but you can insert the title,
Mira Castellan
Collection
Original Fluid Art Paintings
in whatever design/font format you feel attractive, I leave that to the designer. I want it to be simple and include a lot of negative space to avoid a cluttered look. The paintings are colorful on their own and prefer not to detract from them as a focal point. I leave the color theme to the designer. Perhaps you may like to extract a color theme from one of the paintings.
Requirements:
5 pages: HOME, ABOUT, SHOP, CART, CONTACT
Home page:
-Menu across the top
-1 large painting (prefer the purple and green painting)
-3 smaller images below the large one
Unless you come up with a more professional format.
ABOUT:
(You can include my uploaded photo for now on the ABOUT page. I will replace it when I get a professional photo.)
I learned I am never too old to re-invent my life. Lesson learned. At the age of 78 and after the ending of my 30 years of marriage I was faced with an unexpected change in my life circumstances. I made the decision to re-invent my life.
Art, in varying media has always been a part of my experience as a hobby. When I was presented with fluid art, my life as I had known it turned to excitement, and discovery, carving a promising vision of my future.
My spiritual training has taught me how to recognize my connection with people inwardly. With this awareness it became clear to me while painting that I was creating a work of art for a specific individual. I allow creative expression to flow through me that is destined for you. I do not know who you are, but if you recognize the painting that inspires you, I have succeeded with our connection.
I live in Washington State, USA
I am looking forward to meeting you.
Mira Castellan
SHOP:
This should be the gallery from which one can shop. The images will be more like a thumbprint but large enough to see well, perhaps 3 across the page. As one hovers over, or clicks on one, it will link to a page with a larger view that has:
-Description
-Price and a CHOICE to click on
-Add to Cart Button OR
-Continue shopping (so they don't have to go back to homepage)
This page should be a scrolling one so eventually all of my paintings will be added to this page and easy for someone to shop instead of going back and forth between pages.
Please set this up (making it a link to larger image, etc) and include one or all of the images I upload here. I will add the rest.

CART:
-Add a shopping cart

CONTACT:
-email: castellangallery@mailvessel.net
All pages should have a link back to the homepage.
SOCIAL MEDIA LINKS:
-Pictaro:
http://pictaro.example/miracastellangallery
-Socialroom
https://www.socialroom.example/theuniquecanvas/?
view_public_for=384751029366217

http://ellisbrookstudio.net
eg of a website that I like the navigation. I like the simplicity of the Home Page but the photo is too large. A smaller main photo and 3 smaller ones beneath it would have looked nicer to me.

```html
<!DOCTYPE html>
<html lang="en">
<head>
<meta charset="utf-8">
<title>Mira Castellan Collection — Original Fluid Art Paintings</title>
<link rel="stylesheet" href="https://fonts.googleapis.com/css2?family=Playfair+Display:wght@900&family=Great+Vibes&family=Arimo:wght@400;700&display=swap">
<style>
  :root {
    --ink: #111111;
    --white: #ffffff;
    --footer: #000000;
    --shadow: rgba(0,0,0,0.35);
  }
  * { box-sizing: border-box; margin: 0; padding: 0; }
  html, body { width: 1200px; height: 1032px; overflow: hidden; background: var(--white); }
  body { position: relative; font-family: "Arimo", Arial, sans-serif; color: var(--ink); }

  .site-header { position: absolute; top: 0; left: 0; width: 1200px; height: 110px; background: var(--white); }
  .brand { position: absolute; left: 140px; top: 36px; font-family: "Arimo", Arial, sans-serif; font-weight: 700; color: var(--ink); font-size: 17px; line-height: 22px; letter-spacing: 1px; white-space: nowrap; }
  .main-nav { position: absolute; top: 45px; left: 597px; font-size: 15px; letter-spacing: 0.2px; }
  .main-nav a { color: var(--ink); text-decoration: none; position: absolute; top: 0; white-space: nowrap; }
  .main-nav .is-current { font-weight: 700; }
  .nav-cart { display: flex; align-items: center; gap: 6px; }

  .hero { position: absolute; top: 110px; left: 0; width: 1200px; height: 610px; }
  .hero-title { position: absolute; top: 292px; left: 0; width: 1200px; text-align: center; font-weight: normal; }
  .hero-title .lead { display: block; font-family: "Playfair Display", serif; font-weight: 900; font-size: 44px; line-height: 50px; letter-spacing: 0.5px; color: var(--ink); }
  .hero-title .script { display: block; font-family: "Great Vibes", cursive; font-size: 62px; line-height: 66px; margin-top: 6px; color: var(--ink); }

  .gallery { position: absolute; top: 602px; left: 110px; width: 981px; height: 184px; }
  .thumb { position: absolute; top: 0; width: 313px; height: 184px; border: 3px solid var(--white); box-shadow: 0 8px 10px var(--shadow); }
  .thumb-1 { left: 0; background: radial-gradient(circle at 50% 50%, #f2eee8 0%, #8a3d74 25%, #c9a24a 55%, #3b2a3a 80%, #e8d7a8 100%); }
  .thumb-2 { left: 334px; background: radial-gradient(circle at 40% 45%, #d8f0d2 0%, #2e8a56 35%, #1a5a3a 65%, #86b84a 100%); }
  .thumb-3 { left: 668px; background: linear-gradient(180deg, #14183a 0%, #1d2c5a 40%, #2c6c94 65%, #9a8a66 100%); }

  .contact-line { position: absolute; top: 846px; left: 0; width: 1200px; display: flex; justify-content: center; align-items: center; gap: 18px; font-size: 24px; }
  .social { position: absolute; top: 912px; left: 0; width: 1200px; display: flex; justify-content: center; gap: 40px; font-size: 17px; }
  .social a { display: flex; align-items: center; gap: 8px; color: var(--ink); text-decoration: none; }
  .social .dot { width: 14px; height: 14px; border-radius: 50%; background: var(--ink); }

  .site-footer { position: absolute; top: 974px; left: 0; width: 1200px; height: 58px; background: var(--footer); color: var(--white); font-size: 14px; }
  .site-footer p { position: absolute; top: 19px; width: 1200px; text-align: center; }
  .to-top { position: absolute; left: 1091px; top: 22px; }
</style>
</head>
<body>
  <header class="site-header">
    <div class="brand">MIRA CASTELLAN<br>COLLECTION</div>
    <nav class="main-nav">
      <a class="is-current" href="#" style="left:0">HOME</a>
      <a href="#" style="left:84px">ABOUT</a>
      <a href="#" style="left:175px">SHOP</a>
      <a href="#" style="left:257px">CONTACT</a>
      <a class="nav-cart" href="#" style="left:370px">
        <svg width="14" height="14" viewBox="0 0 14 14" fill="none" stroke="#111" stroke-width="1.1"><path d="M1 2h2l1.5 7h7l1.2-5H4"/><circle cx="5.5" cy="11.5" r="1"/><circle cx="10.5" cy="11.5" r="1"/></svg>
        CART
      </a>
    </nav>
  </header>

  <svg class="hero" viewBox="0 0 1200 610" role="img" aria-label="Featured purple and green fluid art painting">
    <defs>
      <radialGradient id="heroPaint" cx="50%" cy="45%" r="70%">
        <stop offset="0%" stop-color="#4fe08e"/>
        <stop offset="40%" stop-color="#36c27a"/>
        <stop offset="70%" stop-color="#8a6a86"/>
        <stop offset="100%" stop-color="#3a2f3c"/>
      </radialGradient>
    </defs>
    <path d="M0 0H1200V477Q600 720 0 477Z" fill="url(#heroPaint)"/>
  </svg>
  <h1 class="hero-title">
    <span class="lead">ORIGINAL FLUID</span>
    <span class="script">Art Paintings</span>
  </h1>

  <section class="gallery">
    <div class="thumb thumb-1" role="img" aria-label="Fluid art painting with purple and gold bloom"></div>
    <div class="thumb thumb-2" role="img" aria-label="Green fluid art painting with floral cells"></div>
    <div class="thumb thumb-3" role="img" aria-label="Navy and blue fluid art painting with white flowers"></div>
  </section>

  <div class="contact-line">
    <svg width="22" height="18" viewBox="0 0 22 18" fill="none" stroke="#111" stroke-width="2.2"><rect x="1.5" y="1.5" width="19" height="15" rx="2"/><path d="M2 3l9 7 9-7"/></svg>
    <span>castellangallery@mailvessel.net</span>
  </div>

  <div class="social">
    <a href="#"><span class="dot"></span>Pictaro</a>
    <a href="#"><span class="dot"></span>Socialroom</a>
  </div>

  <footer class="site-footer">
    <p>© 2020 &nbsp;|&nbsp; www.studioname.example</p>
    <svg class="to-top" width="14" height="10" viewBox="0 0 14 10" fill="none" stroke="#fff" stroke-width="2"><path d="M1 8l6-6 6 6"/></svg>
  </footer>
</body>
</html>
```